American cannabis tech company business card design

Thrum.com is seeking a modern, professional, and brand-aligned business card that represents our company and its core values: Mission, Story, Values, and Impact. As an innovative cannabis company, we want a business card that is not only visually appealing but also serves as a representation of who we are and what we stand for.

Project Scope: Design a double-sided business card that integrates our brand identity and core values. Incorporate our key brand elements, ensuring a sleek and contemporary aesthetic. Visually reflect our core values (Mission, Story, Values, Impact) in a way that is engaging yet professional.

Target Market(s)

Vendors, third parties,

Contact Information for Business Card

Contact details (name, title, email, phone, website, etc.)

Font styles to use
Other font styles liked:
• Caslon, Centra

Colors

Designer to choose colors to be used in the design.

Requirements
Must have
• Thrum.com logo and branding A creative yet clean way to integrate our core values (Mission, Story, Values, Impact) Modern typography and a well-structured layout
Nice to have
• forest green, grey, white, black
Should not have
• references to marijuana, leafs, plants, or related product

```html
<!DOCTYPE html>
<html lang="en">
<head>
<meta charset="utf-8">
<title>Thrum Business Card</title>
<link href="https://fonts.googleapis.com/css2?family=Arimo:wght@400;700&display=swap" rel="stylesheet">
<style>
  :root{
    --page:#16181a;
    --green-deep:#0e2414;
    --green-mid:#16391e;
    --green-light:#1f4d27;
    --line-green:#3f9a4c;
    --white:#ffffff;
    --soft-white:#e9efe9;
    --muted:#b9cfbb;
  }
  *{box-sizing:border-box;margin:0;padding:0}
  html,body{width:1200px;height:840px;overflow:hidden}
  body{
    background:var(--page);
    font-family:"Arimo",Arial,sans-serif;
    display:flex;flex-direction:column;align-items:center;justify-content:center;gap:40px;
  }
  .card{
    position:relative;width:620px;height:354px;border-radius:22px;overflow:hidden;
    box-shadow:0 18px 40px rgba(0,0,0,.55);
  }
  .card-front{
    background:linear-gradient(135deg,var(--green-mid) 0%,var(--green-deep) 55%,var(--green-mid) 100%);
  }
  .contour-field{
    position:absolute;inset:0;
    background:radial-gradient(ellipse 60% 62% at 50% 50%,var(--green-deep) 0%,#15401d 45%,#1b5a26 75%,var(--green-mid) 100%);
  }
  .wordmark{
    font-family:"Arimo",Arial,sans-serif;font-weight:700;color:var(--white);
    letter-spacing:2px;line-height:1;
  }
  .front-lockup{
    position:absolute;left:50%;top:50%;transform:translate(-50%,-50%);
    display:flex;flex-direction:column;align-items:center;gap:18px;
  }
  .card-front .wordmark{font-size:96px}
  .core-values{
    display:flex;gap:14px;list-style:none;
    font-size:12px;font-weight:700;letter-spacing:3px;color:var(--muted);
  }
  .core-values li+li::before{content:"·";margin-right:14px;color:var(--line-green)}
  .card-back{
    background:linear-gradient(160deg,var(--green-light) 0%,var(--green-deep) 45%,var(--green-mid) 100%);
    color:var(--white);
  }
  .card-back .wordmark{position:absolute;left:40px;top:100px;font-size:80px}
  .identity{position:absolute;right:44px;top:32px;text-align:right}
  .identity-bar{position:absolute;right:22px;top:30px;width:6px;height:46px;background:var(--white)}
  .person-name{font-size:22px;font-weight:700;letter-spacing:.5px}
  .person-title{font-size:15px;color:var(--soft-white);margin-top:4px}
  .motif{
    position:absolute;right:40px;top:106px;width:220px;height:200px;border-radius:50%;
    background:radial-gradient(circle,rgba(90,150,90,.35) 0%,rgba(90,150,90,.12) 60%,rgba(90,150,90,0) 75%);
  }
  .contact-block{position:absolute;left:110px;bottom:40px}
  .address{font-size:15px;line-height:1.35;color:var(--soft-white)}
  .contacts{margin-top:12px;list-style:none;font-size:15px;line-height:1.4}
  .contacts li{display:flex;align-items:center;gap:8px}
  .contacts svg{width:13px;height:13px;fill:var(--white);flex:none}
</style>
</head>
<body>
  <section class="card card-front">
    <div class="contour-field" role="img" aria-label="Concentric green contour lines radiating from the wordmark"></div>
    <div class="front-lockup">
      <div class="wordmark">THRUM</div>
      <ul class="core-values">
        <li>MISSION</li>
        <li>STORY</li>
        <li>VALUES</li>
        <li>IMPACT</li>
      </ul>
    </div>
  </section>

  <section class="card card-back">
    <div class="wordmark">THRUM</div>
    <div class="identity-bar"></div>
    <div class="identity">
      <p class="person-name">DANIEL HARPER</p>
      <p class="person-title">Managing Director</p>
    </div>
    <div class="motif" role="img" aria-label="Faint green brand motif illustration"></div>
    <div class="contact-block">
      <p class="address">Your Address<br>City, State, Zip 0000</p>
      <ul class="contacts">
        <li><svg viewBox="0 0 24 24"><path d="M6.6 10.8a15 15 0 0 0 6.6 6.6l2.2-2.2c.3-.3.7-.4 1-.2 1.1.4 2.3.6 3.6.6.6 0 1 .4 1 1V20c0 .6-.4 1-1 1A17 17 0 0 1 3 4c0-.6.4-1 1-1h3.5c.6 0 1 .4 1 1 0 1.3.2 2.5.6 3.6.1.3 0 .7-.2 1z"/></svg>044-555 210 384</li>
        <li><svg viewBox="0 0 24 24"><path d="M2 5h20v14H2zm2 2v.5l8 5 8-5V7zm0 2.8V17h16V9.8l-8 5z"/></svg>hello@thrum.com</li>
        <li><svg viewBox="0 0 24 24"><path d="M12 2a10 10 0 1 0 0 20 10 10 0 0 0 0-20zm6.9 6h-3a15 15 0 0 0-1.3-4A8 8 0 0 1 18.9 8zM12 4c.8 1.2 1.5 2.5 1.9 4h-3.8c.4-1.5 1.1-2.8 1.9-4zM4.3 14a8 8 0 0 1 0-4h3.4a16 16 0 0 0 0 4zm.8 2h3a15 15 0 0 0 1.3 4A8 8 0 0 1 5.1 16zm3-8h-3a8 8 0 0 1 4.3-4 15 15 0 0 0-1.3 4zM12 20c-.8-1.2-1.5-2.5-1.9-4h3.8c-.4 1.5-1.1 2.8-1.9 4zm2.3-6H9.7a14 14 0 0 1 0-4h4.6a14 14 0 0 1 0 4zm.3 6a15 15 0 0 0 1.3-4h3a8 8 0 0 1-4.3 4zm1.7-6a16 16 0 0 0 0-4h3.4a8 8 0 0 1 0 4z"/></svg>www.thrum.com</li>
      </ul>
    </div>
  </section>
</body>
</html>
```